Clean, Fresh Business Card Design Needed

We need a business card design for a new business we have taken over called "Bonders and Fixers". We got a logo through this website which i have attached. We are wanting something that is vibrant but clean and fresh. Our business mainly sells glue. Maybe a cool design/slogan on the back? Modern, sleek.

Industry/Entity Type

Business

Contact Information for Business Card

Name: Derek Tamsin, Managing Director. Address: 164 Kowhai Lane, Tauranga 3112, Phone: 07 549 2361 Mobile: 021 634 915 Fax: 07 549 2874 Email: bond.fix@mailvo.co.nz, Web: www.tackbondpro.co.nz

Font styles to use
Serif

Requirements
Must have
• All business card details, logo.
Nice to have
• Design, slogan on back of card

```html
<!DOCTYPE html>
<html lang="en">
<head>
<meta charset="utf-8">
<title>Bonders and Fixers — Business Card</title>
<link rel="stylesheet" href="https://fonts.googleapis.com/css2?family=Cinzel:wght@400&family=Poppins:ital,wght@0,400;0,600;1,400&display=swap">
<style>
  :root {
    --navy: #34306b;
    --navy-deep: #2c2860;
    --navy-soft: #3f3b78;
    --paper: #f4f4f6;
    --paper-shade: #e9e9ee;
    --ink: #2a2a3a;
    --ink-muted: #555566;
    --backdrop: #e4e4e6;
  }
  * { box-sizing: border-box; margin: 0; padding: 0; }
  html, body { width: 1200px; height: 726px; overflow: hidden; }
  body {
    background: var(--backdrop);
    font-family: "Poppins", sans-serif;
    position: relative;
  }
  .card {
    position: absolute;
    top: 208px;
    width: 540px;
    height: 310px;
    overflow: hidden;
    box-shadow: 0 4px 14px rgba(0,0,0,0.12);
  }
  /* Front */
  .card-front { left: 40px; background: var(--navy); }
  .front-decoration {
    position: absolute; right: -40px; top: -30px;
    width: 260px; height: 300px;
    border-radius: 48% 52% 40% 60%;
    background: radial-gradient(circle at 40% 40%, var(--navy-soft), rgba(63,59,120,0) 70%);
  }
  .front-brand {
    position: absolute; left: 0; right: 0; top: 92px;
    display: flex; flex-direction: column; align-items: center; gap: 16px;
  }
  .brand-square {
    width: 56px; height: 56px; border-radius: 6px; background: #ffffff;
  }
  .front-brand .brand-name {
    font-family: "Cinzel", serif; font-weight: 400;
    color: #ffffff; font-size: 30px; letter-spacing: 3px;
  }
  /* Back */
  .card-back { left: 620px; background: var(--paper); }
  .back-decoration {
    position: absolute; right: 20px; top: -20px;
    width: 200px; height: 200px; border-radius: 50% 45% 55% 50%;
    background: radial-gradient(circle at 50% 50%, var(--paper-shade), rgba(233,233,238,0) 70%);
  }
  .back-brand {
    position: absolute; left: 32px; top: 52px;
    display: flex; align-items: center; gap: 10px;
  }
  .back-brand .brand-square { width: 40px; height: 40px; border-radius: 4px; background: var(--navy); }
  .back-brand .brand-name {
    font-family: "Cinzel", serif; font-weight: 400; color: var(--ink); font-size: 19px; letter-spacing: 1.5px;
  }
  .rule {
    position: absolute; left: 150px; top: 150px; width: 390px; height: 1.5px; background: var(--navy);
  }
  .side-bar { position: absolute; left: 0; top: 140px; width: 6px; height: 60px; background: var(--navy); }
  .person { position: absolute; left: 32px; top: 138px; }
  .person-name { font-weight: 600; font-size: 15px; color: var(--ink); }
  .person-role { font-style: italic; font-size: 11px; color: var(--ink-muted); margin-top: 2px; }
  .phones { position: absolute; left: 32px; top: 212px; list-style: none; }
  .phones li, .details li {
    display: flex; align-items: center; gap: 7px;
    font-size: 12px; color: var(--ink); line-height: 18px;
  }
  .details {
    position: absolute; right: 24px; top: 74px; list-style: none; text-align: right;
  }
  .details li { justify-content: flex-end; font-size: 11px; }
  .icon { width: 11px; height: 11px; fill: var(--navy); flex: none; }
  .bottom-band { position: absolute; left: 0; right: 0; bottom: 0; height: 20px; background: var(--navy); }
</style>
</head>
<body>
  <section class="card card-front" aria-label="Card front">
    <div class="front-decoration" role="img" aria-label="Faint glue splash decoration"></div>
    <div class="front-brand">
      <div class="brand-square"></div>
      <div class="brand-name">Bonders and Fixers</div>
    </div>
  </section>

  <section class="card card-back" aria-label="Card back">
    <div class="back-decoration" role="img" aria-label="Faint glue splash decoration"></div>
    <div class="back-brand">
      <div class="brand-square"></div>
      <div class="brand-name">Bonders and Fixers</div>
    </div>

    <ul class="details">
      <li>bond.fix@mailvo.co.nz
        <svg class="icon" viewBox="0 0 12 12"><rect x="0" y="2" width="12" height="8" rx="1"/><path d="M0.5 2.5 L6 7 L11.5 2.5" fill="none" stroke="#fff" stroke-width="1"/></svg></li>
      <li>www.tackbondpro.co.nz
        <svg class="icon" viewBox="0 0 12 12"><circle cx="6" cy="6" r="5.5"/><path d="M0.5 6h11M6 0.5c-3 3-3 8 0 11M6 0.5c3 3 3 8 0 11" fill="none" stroke="#fff" stroke-width="0.8"/></svg></li>
      <li>164 Kowhai Lane, Tauranga 3112
        <svg class="icon" viewBox="0 0 12 12"><path d="M6 0.5a4 4 0 0 0-4 4c0 3 4 7 4 7s4-4 4-7a4 4 0 0 0-4-4z"/><circle cx="6" cy="4.5" r="1.5" fill="#fff"/></svg></li>
    </ul>

    <div class="rule"></div>
    <div class="side-bar"></div>
    <div class="person">
      <div class="person-name">Derek Tamsin</div>
      <div class="person-role">Manager</div>
    </div>

    <ul class="phones">
      <li><svg class="icon" viewBox="0 0 12 12"><rect x="3" y="0.5" width="6" height="11" rx="1"/><rect x="4" y="2" width="4" height="7" fill="#fff"/></svg>021 634 915</li>
      <li><svg class="icon" viewBox="0 0 12 12"><path d="M1 4c0-2 2-3 5-3s5 1 5 3v1H8V4H4v1H1z"/><rect x="2" y="6" width="8" height="5" rx="1"/></svg>07 549 2361</li>
      <li><svg class="icon" viewBox="0 0 12 12"><rect x="3" y="0.5" width="6" height="4"/><rect x="1" y="4" width="10" height="5" rx="1"/><rect x="3" y="8" width="6" height="3.5"/></svg>07 549 2874</li>
    </ul>

    <div class="bottom-band"></div>
  </section>
</body>
</html>
```